Need innovative card design for tech start up

We are a Santa Monica based marketing analytics software start up called Meridel Pulse. We're launching a platform that will help advertisers better measure and optimize their marketing spend by using advanced algorithmic analytic. While our subject matter is complicated, we want to convey simple, clean, curated. We also want to stand out - ad tech is a sea of sameness and we need to have some individuality. We have an established color palette and would like to see a design we could print in each tone (teal, tangerine, grey), but it doesn't require the card to be monochromatic. The font used is DENSE.

Marketing

```html
<!DOCTYPE html>
<html lang="en">
<head>
<meta charset="utf-8">
<title>Meridel Pulse – Business Card</title>
<link rel="stylesheet" href="https://fonts.googleapis.com/css2?family=Open+Sans:wght@400;700&family=Roboto+Condensed:wght@300&display=swap">
<style>
  :root {
    --tangerine: #f7941d;
    --paper: #ffffff;
    --ink-grey: #6b6b6b;
    --text-grey: #555555;
    --backdrop: #ecebe8;
  }
  * { margin: 0; padding: 0; box-sizing: border-box; }
  html, body { width: 1200px; height: 784px; overflow: hidden; }
  body {
    background: var(--backdrop);
    position: relative;
    font-family: "Open Sans", Arial, sans-serif;
  }
  .card {
    position: absolute;
    width: 540px;
    height: 309px;
    overflow: hidden;
    box-shadow: 0 4px 14px rgba(0,0,0,0.12);
  }
  /* Front side */
  .card-front { left: 50px; top: 90px; background: var(--tangerine); }
  .card-front .wordmark {
    position: absolute;
    left: 34px; top: 136px;
    font-family: "Roboto Condensed", "Arial Narrow", sans-serif;
    font-weight: 300;
    font-size: 30px;
    letter-spacing: 0.5px;
    color: var(--ink-grey);
    text-transform: uppercase;
    white-space: nowrap;
  }
  .card-front .accent-circle {
    position: absolute;
    left: 300px; top: 28px;
    width: 250px; height: 250px;
    border-radius: 50%;
    background: var(--paper);
  }
  /* Back side */
  .card-back { left: 610px; top: 385px; background: var(--paper); }
  .holder {
    position: absolute;
    right: 24px; top: 20px;
    text-align: right;
  }
  .holder-name { font-size: 14px; font-weight: 700; color: var(--tangerine); }
  .holder-title { font-size: 10px; color: var(--text-grey); margin-top: 1px; }
  .brand-square {
    position: absolute;
    left: 28px; top: 50px;
    width: 92px; height: 92px;
    background: var(--tangerine);
  }
  .rule-upper {
    position: absolute;
    left: 120px; right: 0; top: 118px;
    height: 4px;
    background: var(--tangerine);
  }
  .brand-name {
    position: absolute;
    left: 28px; top: 145px;
    font-family: "Roboto Condensed", "Arial Narrow", sans-serif;
    font-weight: 300;
    font-size: 19px;
    line-height: 22px;
    color: var(--ink-grey);
    text-transform: uppercase;
    white-space: nowrap;
  }
  .rule-lower {
    position: absolute;
    left: 0; right: 0; top: 172px;
    height: 4px;
    background: var(--tangerine);
  }
  .contact-list {
    position: absolute;
    left: 30px; top: 184px;
    list-style: none;
    font-size: 14px;
    line-height: 18px;
    color: var(--text-grey);
    white-space: nowrap;
  }
  .contact-list li { display: flex; align-items: center; gap: 7px; }
  .contact-list svg { width: 13px; height: 13px; fill: var(--tangerine); flex: none; }
  .contact-list .indent { padding-left: 20px; }
</style>
</head>
<body>

<section class="card card-front" aria-label="Card front">
  <div class="wordmark">Meridel Pulse</div>
  <div class="accent-circle"></div>
</section>

<section class="card card-back" aria-label="Card back">
  <div class="holder">
    <div class="holder-name">Dorian Falkner</div>
    <div class="holder-title">Founder/CEO</div>
  </div>
  <div class="brand-square"></div>
  <div class="rule-upper"></div>
  <div class="brand-name">Meridel Pulse</div>
  <div class="rule-lower"></div>
  <ul class="contact-list">
    <li><svg viewBox="0 0 24 24"><path d="M6.6 10.8a15.1 15.1 0 0 0 6.6 6.6l2.2-2.2a1 1 0 0 1 1-.25 11.4 11.4 0 0 0 3.6.57 1 1 0 0 1 1 1V20a1 1 0 0 1-1 1A17 17 0 0 1 3 4a1 1 0 0 1 1-1h3.5a1 1 0 0 1 1 1c0 1.25.2 2.45.57 3.57a1 1 0 0 1-.25 1z"/></svg>805-555-0147 x204</li>
    <li><svg viewBox="0 0 24 24"><path d="M7 1h10a2 2 0 0 1 2 2v18a2 2 0 0 1-2 2H7a2 2 0 0 1-2-2V3a2 2 0 0 1 2-2zm0 3v13h10V4zm5 15a1.3 1.3 0 1 0 0 2.6 1.3 1.3 0 0 0 0-2.6z"/></svg>805-555-0183</li>
    <li><svg viewBox="0 0 24 24"><path d="M2 5h20v14H2zm2 2v.4l8 5.2 8-5.2V7zm0 2.8V17h16V9.8l-8 5.2z"/></svg>dorian@meridelpulse.com</li>
    <li><svg viewBox="0 0 24 24"><path d="M12 2a10 10 0 1 0 0 20 10 10 0 0 0 0-20zm6.9 9h-3a15 15 0 0 0-1.4-6.1A8 8 0 0 1 18.9 11zM12 4.1A13 13 0 0 1 13.9 11h-3.8A13 13 0 0 1 12 4.1zM9.5 4.9A15 15 0 0 0 8.1 11h-3a8 8 0 0 1 4.4-6.1zM5.1 13h3a15 15 0 0 0 1.4 6.1A8 8 0 0 1 5.1 13zm6.9 6.9a13 13 0 0 1-1.9-6.9h3.8a13 13 0 0 1-1.9 6.9zm2.5-.8a15 15 0 0 0 1.4-6.1h3a8 8 0 0 1-4.4 6.1z"/></svg>www.meridelpulse.com</li>
    <li><svg viewBox="0 0 24 24"><path d="M12 3 2 12h3v8h5v-6h4v6h5v-8h3z"/></svg>1840 Harbor Crest, suite 310</li>
    <li class="indent">Larkspur Bay, CA 93112</li>
  </ul>
</section>

</body>
</html>
```